OCD Educational Handout

I am looking for a designer to take the educational content I have created about Obsessive Compulsive Disorder and turn it into a nice-looking handout, including managing the font, layout, colors, images, illustrations, and diagrams. I would like the final product to be something I can email clients as a pdf, print out, as well as post on my website. I would like to have the final copy in a form that I can edit should I choose to adjust the content. I want the handout to be professional but also approachable to someone suffering from this disorder. I like the idea of little illustrations almost cartoon like. Almost like little doodles or something. I will have a series of handouts like this that I would want the same designer to help with, and continue with the same design style.

graphic design images and illustrations, and one or two

```html
<!DOCTYPE html>
<html lang="en">
<head>
<meta charset="utf-8">
<title>OCD Educational Handout</title>
<link rel="stylesheet" href="https://fonts.googleapis.com/css2?family=Cinzel:wght@400;600;700&family=Cormorant+Garamond:wght@500;600&family=Great+Vibes&family=Montserrat:wght@400;500;600;700&family=Poppins:wght@400;500;600&display=swap">
<style>
:root{
  --rust:#a65a4a;
  --rust-dark:#8f4a3c;
  --rust-soft:#e9b8a8;
  --rust-light:#fbe6dc;
  --teal:#4d8297;
  --teal-deep:#2f6276;
  --sky:#dbedf5;
  --sky-band:#c5dde7;
  --beige:#f4ebdb;
  --cream:#efe3cc;
  --ink:#2b2b2b;
  --ink-soft:#4a4a4a;
  --backdrop:#b9b9b9;
  --paper:#ffffff;
}
*{margin:0;padding:0;box-sizing:border-box}
html,body{width:1200px;height:2171px;overflow:hidden}
body{background:var(--backdrop);position:relative;font-family:"Montserrat",sans-serif;color:var(--ink)}
.page{position:absolute;background:var(--paper);overflow:hidden}
.abs{position:absolute}
.body-text{font-family:"Poppins",sans-serif;font-size:5.6px;line-height:1.38;color:var(--ink-soft)}
.body-text p{margin-bottom:4px}
.body-text strong{color:var(--ink);font-weight:600}
.placeholder{position:absolute}

/* ---------- cover spread ---------- */
.cover{left:116px;top:99px;width:965px;height:626px;background:linear-gradient(180deg,#f6fbfd 0%,#e4f1f7 55%,var(--sky-band) 62%,#b7d3df 100%)}
.cover .band{left:0;top:388px;width:965px;height:238px;background:linear-gradient(180deg,#cde2ea 0%,#b9d4df 100%)}
.brand-mark{display:flex;flex-direction:column;align-items:center;gap:4px}
.brand-mark .dot{width:84px;height:84px;border-radius:50%;background:#b9d7e1}
.brand-mark .name{font-family:"Cinzel",serif;font-size:9.5px;color:var(--ink);letter-spacing:.6px}
.brand-mark.small .dot{width:56px;height:56px;background:#2b2b2b}
.brand-mark.small .name{font-size:6.5px}
.therapist-name{font-family:"Cinzel",serif;font-size:19px;color:var(--rust);font-weight:600;letter-spacing:.5px}
.therapist-rule{width:145px;height:1px;background:var(--rust-soft);margin:5px 0 7px}
.therapist-cred{font-family:"Cormorant Garamond",serif;font-size:18px;letter-spacing:5px;color:var(--ink)}
.contact-list{list-style:none;margin-top:10px}
.contact-list li{display:flex;align-items:center;gap:9px;font-family:"Poppins",sans-serif;font-weight:500;font-size:11px;color:var(--ink);height:28px}
.contact-list svg{width:12px;height:12px;flex:none}
.welcome{font-family:"Great Vibes",cursive;font-size:31px;color:var(--ink);text-align:center;width:420px}
.freedom{font-family:"Cinzel",serif;font-weight:700;font-size:38px;color:var(--teal);letter-spacing:.5px;text-align:center;width:420px;line-height:1}
.from-ocd{background:var(--rust);color:#fff;font-family:"Cinzel",serif;font-size:31px;text-align:center;line-height:36px;letter-spacing:3px}
.from-ocd b{font-weight:700}
.cover-url{font-family:"Montserrat",sans-serif;font-size:15px;letter-spacing:2.6px;font-weight:500;color:var(--ink);text-align:center;width:420px}
.cover-url b{font-weight:700}

/* ---------- shared headings ---------- */
.sec-title{font-family:"Cinzel",serif;color:var(--rust);font-size:11.5px;font-weight:600;line-height:1.1;white-space:nowrap}
.sec-title.on-rust{color:var(--rust-light)}
.sec-title.dark{color:var(--ink)}

/* ---------- spread two ---------- */
.inside-one{left:122px;top:769px;width:955px;height:617px}
.intro-lead{font-family:"Montserrat",sans-serif;font-size:7px;font-weight:600;line-height:1.35;color:var(--ink);margin-bottom:7px}
.intro-lead em{color:var(--rust);font-style:normal}
.panel-beige{background:var(--beige);border-radius:0 10px 10px 0}
.panel-sky{background:var(--sky);border-radius:8px}
.num-tag{display:flex;align-items:center;gap:2px}
.num-tag .num{font-family:"Cinzel",serif;font-size:14px;font-weight:700;color:var(--rust);line-height:1}
.num-tag .pill{background:var(--rust);color:#fff;font-family:"Montserrat",sans-serif;font-size:6.4px;font-weight:700;letter-spacing:.8px;padding:2px 8px;width:125px}
.pill-wide{background:var(--rust);color:#fff;font-family:"Montserrat",sans-serif;font-size:6.4px;font-weight:700;letter-spacing:.4px;padding:2px 7px;border-radius:5px;text-align:center}
.tab-head{background:var(--rust);color:#fff;font-family:"Cinzel",serif;font-weight:600;font-size:11.5px;padding:5px 14px;border-radius:8px 0 0 0;clip-path:polygon(0 0,92% 0,100% 100%,0 100%);white-space:nowrap}
.bullets{list-style:none}
.bullets li{position:relative;padding-left:10px;margin-bottom:5px}
.bullets li::before{content:"";position:absolute;left:0;top:1.6px;width:4px;height:4px;border-radius:50%;border:1.2px solid var(--teal)}
.bullets li b{display:block;color:var(--ink);font-weight:600}

/* ---------- spread three ---------- */
.inside-two{left:115px;top:1431px;width:969px;height:628px}
.side-rust{left:0;top:0;width:237px;height:628px;background:var(--rust)}
.phys-item{display:flex;gap:12px;margin-bottom:11px}
.phys-item .icon{width:14px;height:14px;border:1.4px solid #fff;border-radius:3px;flex:none;margin-top:2px;position:relative}
.phys-item .icon::after{content:"";position:absolute;left:3px;top:3px;width:5px;height:5px;border-radius:50%;background:#fff}
.phys-item h4{font-family:"Poppins",sans-serif;font-size:6.8px;font-weight:600;color:#fff}
.phys-item p{font-family:"Poppins",sans-serif;font-size:5.5px;line-height:1.35;color:#f5d9cf}
.rumination-box{border:1.2px solid var(--ink-soft);border-radius:6px;background:#fff;padding:9px 9px}
.rumination-box .t1{font-family:"Cinzel",serif;font-size:11px;color:var(--ink);font-weight:600;line-height:1}
.rumination-box .t2{font-family:"Cinzel",serif;font-size:11px;color:var(--rust);font-weight:600;line-height:1.1;margin-bottom:6px}
.cycle-label{font-family:"Poppins",sans-serif;font-size:4.6px;letter-spacing:.4px;fill:var(--ink)}
</style>
</head>
<body>

<!-- ================= COVER SPREAD ================= -->
<section class="page cover" aria-label="Handout cover">
  <div class="abs band"></div>

  <svg class="abs" style="left:100px;top:95px" width="295" height="295" viewBox="0 0 295 295" aria-hidden="true">
    <circle cx="147" cy="147" r="139" fill="none" stroke="var(--rust)" stroke-width="11"/>
    <circle cx="147" cy="147" r="132" fill="none" stroke="var(--rust-soft)" stroke-width="3"/>
  </svg>
  <div class="placeholder" role="img" aria-label="Illustration of a client on a sofa talking with a therapist, a tangled thought bubble above" style="left:117px;top:112px;width:261px;height:261px;border-radius:50%;background:radial-gradient(circle at 50% 40%,#fbf4f1 0%,#ece3e2 60%,#d9cfcf 100%)"></div>

  <div class="abs brand-mark" style="left:461px;top:30px;width:200px">
    <span class="dot"></span>
    <span class="name">CLEARPATH THERAPY</span>
  </div>

  <svg class="abs" style="left:600px;top:56px" width="372" height="372" viewBox="0 0 372 372" aria-hidden="true">
    <circle cx="186" cy="186" r="183" fill="none" stroke="var(--rust)" stroke-width="1.4"/>
    <path d="M186 16 A170 170 0 0 0 186 356" fill="none" stroke="var(--rust)" stroke-width="16"/>
    <path d="M186 16 A170 170 0 0 1 186 356" fill="none" stroke="var(--cream)" stroke-width="16"/>
  </svg>
  <div class="placeholder" role="img" aria-label="Illustration of a person sitting with head in hands, surrounded by anxious doodles and thought scribbles" style="left:630px;top:86px;width:312px;height:312px;border-radius:50%;background:radial-gradient(circle at 50% 45%,#ffffff 0%,#f1eef6 55%,#dfe0ea 100%)"></div>

  <div class="placeholder" role="img" aria-label="Portrait photograph of the therapist in a blue blazer" style="left:0;top:339px;width:200px;height:287px;background:linear-gradient(180deg,#c3d4dc 0%,#7a8ea6 45%,#2f4d7a 100%)"></div>

  <div class="abs" style="left:202px;top:444px">
    <div class="therapist-name">DANIEL MERCER</div>
    <div class="therapist-rule"></div>
    <div class="therapist-cred">LCSW</div>
    <ul class="contact-list">
      <li><svg viewBox="0 0 12 12"><circle cx="6" cy="6" r="6" fill="var(--rust)"/><path d="M4 3.2l1 1.4-.6.7c.4.8 1 1.4 1.8 1.8l.7-.6 1.4 1-.5 1.1c-2.4-.3-4.3-2.2-4.6-4.6z" fill="#fff"/></svg>555-014-2290</li>
      <li><svg viewBox="0 0 12 12"><circle cx="6" cy="6" r="6" fill="var(--rust)"/><rect x="3" y="4" width="6" height="4.2" fill="none" stroke="#fff" stroke-width=".8"/><path d="M3 4l3 2.3L9 4" fill="none" stroke="#fff" stroke-width=".8"/></svg>daniel@clearpaththerapy.com</li>
      <li><svg viewBox="0 0 12 12"><circle cx="6" cy="6" r="6" fill="var(--rust)"/><circle cx="6" cy="6" r="3" fill="none" stroke="#fff" stroke-width=".8"/><path d="M3 6h6M6 3c-1.2 1.8-1.2 4.2 0 6M6 3c1.2 1.8 1.2 4.2 0 6" fill="none" stroke="#fff" stroke-width=".6"/></svg>www.clearpaththerapy.com</li>
    </ul>
  </div>
  <div class="abs brand-mark small" style="left:369px;top:440px;width:100px">
    <span class="dot"></span>
    <span class="name">CLEARPATH THERAPY</span>
  </div>

  <div class="abs welcome" style="left:516px;top:443px">Welcome to Your First Step</div>
  <div class="abs freedom" style="left:516px;top:479px">TOWARDS FREEDOM</div>
  <div class="abs from-ocd" style="left:604px;top:520px;width:242px">FROM <b>OCD</b></div>
  <div class="abs cover-url" style="left:516px;top:583px">www.<b>clearpaththerapy</b>.com</div>
</section>

<!-- ================= INSIDE SPREAD ONE ================= -->
<section class="page inside-one" aria-label="Understanding OCD and obsessions">
  <div class="abs body-text" style="left:30px;top:27px;width:415px">
    <p class="intro-lead">You've just embarked on an important journey—a journey towards understanding, managing, and reclaiming your life from Obsessive-Compulsive Disorder (OCD). The first and most crucial step on this path is to learn about and study <em>OCD itself.</em></p>
    <p>Understanding OCD is akin to mapping the terrain of an unfamiliar landscape. Just as a map provides insight into the terrain ahead, learning about OCD equips you to navigate your journey with greater awareness, insight and preparedness. By learning about the nature of obsessions and compulsions, the mechanisms that fuel the OCD cycle, and the various forms OCD can take, you're arming yourself with the tools needed to begin dismantling the power that OCD has over your life.</p>
    <p>This initial step is not just about acquiring information; it's about transforming that knowledge into strength, and eventually, into a strategic game plan. The first step is about shifting from a stance of feeling overwhelmed and controlled by OCD, to one of curiosity, openness and empowerment.</p>
    <p>Taking this first step by choosing to learn about OCD is a testament to your resilience and your commitment to your well-being. It marks the beginning of your journey towards freedom from OCD's grip. As you proceed through this information, keep in mind that every piece of information you gather is a tool in your arsenal against OCD, a step towards understanding your opponent, and ultimately, a step towards victory. Revisit this material as often as needed. OCD can be confusing, and even after years of helping individuals recover from OCD, I still have to remind myself of the basic fundamentals every now and again.</p>
    <p>Take notes and write down questions. Bring them with you to your next session. There are no dumb questions. The more you understand your own OCD symptoms, the better.</p>
  </div>

  <div class="abs panel-beige" style="left:0;top:198px;width:478px;height:253px"></div>
  <svg class="abs" style="left:-8px;top:214px" width="218" height="218" viewBox="0 0 218 218" aria-hidden="true">
    <circle cx="109" cy="109" r="104" fill="none" stroke="var(--rust)" stroke-width="7"/>
  </svg>
  <div class="placeholder" role="img" aria-label="Illustration of two people in blue armchairs having a conversation with a question-mark speech bubble" style="left:0;top:226px;width:196px;height:194px;border-radius:0 50% 50% 0;background:radial-gradient(circle at 45% 55%,#eef4fb 0%,#dbe7f5 55%,#b9cff0 100%)"></div>

  <div class="abs body-text" style="left:219px;top:211px;width:248px">
    <div class="sec-title" style="margin-bottom:6px">WHAT IS OCD?</div>
    <p>Obsessive-Compulsive Disorder (OCD) is a common, chronic mental health condition characterized by distressing, persistent thoughts (obsessions) and repetitive behaviors or mental acts (compulsions) that an individual feels compelled to perform. OCD is a relatively common mental health condition affecting an estimated 2-3% of the population. The age of onset ranges from early childhood through adulthood. Most common onset age is between 12-24 years old. Males generally develop the disorder between ages 13-15, while the average female onset is a bit later from ages 20-24. Among adults, the prevalence of OCD is equal for men and women. Onset of OCD is most often gradual, although in some cases acute onset has been reported.</p>
    <p>Without treatment the course of OCD is chronic, with varying and changing degrees of severity over time. The chronic nature of OCD means that without treatment, symptoms are likely to progress and worsen as time goes on.</p>
    <p>OCD has a significant impact on one's life. Dealing with obsessions and compulsions for hours each day leads to severe personal distress and interferes with employment, relationships, and daily activities. Between 80% and 100% report significant difficulties and impairment in home, work, relationships, and social life.</p>
    <div class="sec-title" style="margin:7px 0 5px;font-size:9.6px">HOW DOES OCD OPERATE IN THE BRAIN?</div>
    <p>Research suggests that OCD involves communication issues between different parts of the brain, including the amygdala, which plays a key role in processing emotions. The amygdala is responsible for regulating fear and is the center of the fight or flight system. OCD can be conceptualized as a malfunctioning alarm system. Imagine a fire alarm going off when there is no actual fire.</p>
  </div>

  <div class="abs body-text" style="left:26px;top:473px;width:200px">
    <div class="sec-title" style="margin-bottom:6px">WHAT ARE OBSESSIONS?</div>
    <p>Obsessions are a core component of Obsessive-Compulsive Disorder (OCD), manifesting as recurrent, persistent thoughts, urges, or images that are intrusive and unwanted. These thoughts are beyond the individual's control and cause significant emotional and psychological distress. Unlike everyday worries or concerns, obsessions in OCD are intense and pervasive, often seeming irrational or exaggerated to the person experiencing them. OCD was once referred to as the 'Doubting Disease' because of its insidious ability to instill doubt and uncertainty into almost any aspect of a person's existence. It should be noted that nothing is off limits to OCD. Symptoms commonly include fears of contamination, upsetting thoughts about sex, morality, perfection, violence, death, religion, relationships and one's personal identity.</p>
  </div>
  <div class="abs body-text" style="left:239px;top:468px;width:217px">
    <div class="pill-wide" style="width:175px;margin-bottom:6px">EGO DYSTONIC NATURE OF OBSESSIONS</div>
    <p>A key characteristic of many obsessions is their ego-dystonic nature, meaning they are not in harmony with an individual's self-perception, values, or desired thoughts. Individuals recognize that their obsessions are a product of their mind that do not reflect their true desires or intentions, yet they feel powerless to stop them. For example, an individual may have a thought to harm someone they love or care about, despite having no authentic desire to harm this person. Or they may experience an urge to do something they authentically don't wish to do. This discrepancy is often what causes the distress associated with obsessions. It can be rather frightening when we suddenly have a thought that seems so strange, inappropriate, or frightening. They can be difficult to dismiss.</p>
  </div>

  <div class="abs sec-title" style="left:508px;top:27px">HOW ARE OBSESSIONS EXPERIENCED?</div>
  <div class="abs body-text" style="left:508px;top:50px;width:200px">
    <div class="num-tag" style="margin-bottom:6px"><span class="num">1</span><span class="pill">INTRUSIVE THOUGHTS</span></div>
    <p>These are unwanted, recurrent thoughts and ideas that pop into a person's mind. They can be about anything, but are always unsettling and result in some kind of emotional distress. They often target a person's sense of self, threatening some pending catastrophe, or involve something terrible happening.</p>
    <p><strong>Examples:</strong><br>What if I left the stove on and the house burns down? What if I am responsible for getting my grandmother sick? What if I lose control and hurt someone? What if I contract some disease? What if I'm not the person I think I am? What if someone dies because I make a mistake? What if I harm a bad person? What if I didn't lock the door and someone breaks into my house and hurts my family? What if I hit someone while I was driving and didn't realize it? What if I am a pedophile? What if I am crazy? What if I don't really love my partner? What if I get canceled? What if I have done something harmful in my past and can't remember it? What if I blurt out something hurtful during this meeting? What if I jump off this balcony or push my partner off? etc.</p>
    <div class="num-tag" style="margin:6px 0"><span class="num">2</span><span class="pill">INTRUSIVE SENSATIONS</span></div>
    <p>These are unwanted sensations in the body, or a hyperawareness to normal automatic processes such as heartbeat, vision, swallowing, blinking, breathing etc. These can also include sensations in the body that feel "not right" or "off" in some way.</p>
  </div>
  <div class="abs body-text" style="left:730px;top:50px;width:205px">
    <div class="num-tag" style="margin-bottom:6px"><span class="num">3</span><span class="pill">INTRUSIVE IMAGES</span></div>
    <p>These are unwanted, recurrent images that pop into a person's awareness. They are experienced in the mind's eye vs. the actual eye. They can be about anything, but are always unsettling and result in some form of emotional distress.</p>
    <p><strong>Examples:</strong><br>Inappropriate or taboo sexual images, graphic and violent images, and images that one would find disgusting or displeasing.</p>
    <div class="num-tag" style="margin:6px 0"><span class="num">4</span><span class="pill">INTRUSIVE URGES</span></div>
    <p>These are sensations and feelings within the body and mind that one concludes are urges to act on an unwanted impulse. It should be noted that the individual has no true desire to act on the urge, however the urge itself is frightening to the individual.</p>
    <p><strong>Examples:</strong><br>Urge to jump into traffic, urge to harm the person next to them, urge to blurt out something inappropriate, urge to drive into traffic.</p>
    <div class="num-tag" style="margin:6px 0"><span class="num">5</span><span class="pill">INTRUSIVE FEELINGS</span></div>
    <p>Intrusive sudden experiences of fear, guilt, shame, doom, panic, and disgust etc. (despite there being no apparent or objective reason for the feeling).</p>
  </div>

  <div class="abs panel-sky" style="left:508px;top:297px;width:424px;height:296px"></div>
  <div class="abs tab-head" style="left:508px;top:297px;width:230px">WHAT ARE COMPULSIONS?</div>
  <div class="abs body-text" style="left:522px;top:325px;width:400px">
    <p>Compulsions, or sometimes referred to as rituals, are repetitive behaviors or mental acts that an individual with Obsessive-Compulsive Disorder (OCD) feels driven to perform in response to an obsession or according to rigidly applied rules. The primary function of compulsions is to reduce emotional distress or prevent some feared outcome or situation; however, these compulsions are not realistically connected to what they are designed to neutralize or prevent, or they are clearly excessive and very time consuming.</p>
  </div>
  <ul class="abs bullets body-text" style="left:522px;top:371px;width:185px">
    <li>Compulsions and Rituals are an attempt to cope and manage the intense anxiety and distress caused by the obsessions. They are an attempt to neutralize the fear and/or prevent a feared outcome.</li>
    <li>They offer temporary relief, although it is short lived. Often, once a compulsion is completed, the person feels compelled to repeat it again and again. The more compulsions a person does, the stronger the OCD gets in the long term.</li>
    <li>Compulsions often become more complex and more time consuming as the disorder progresses. Maybe a person only had to wash their hands for 30 seconds at first, but two months later they must wash for 12 minutes. Or maybe a person only had to say one prayer after having a scary thought, but after several months they must repeat it 20 times to get the same relief.</li>
    <li>Compulsions are not automatic, they are a voluntary attempt to reduce distress and prevent a feared outcome. Despite a person feeling compelled to perform the compulsion, they are still within a person's control. Whereas Obsessions (intrusive thoughts) are completely outside a person's control.</li>
    <li>Reducing and eventually eliminating compulsions is an important part of treatment, and what eventually breaks the OCD cycle and leads to long term relief.</li>
  </ul>
  <div class="placeholder" role="img" aria-label="Illustration of a worried person in a dark cloud holding a balance scale, with small figures on each side" style="left:711px;top:372px;width:215px;height:212px;border-radius:46% 50% 42% 48%;background:radial-gradient(circle at 50% 50%,#3b4a6b 0%,#23304d 70%,#1b2540 100%)"></div>
</section>

<!-- ================= INSIDE SPREAD TWO ================= -->
<section class="page inside-two" aria-label="Compulsions, avoidance and the OCD cycle">
  <div class="abs side-rust"></div>
  <div class="abs" style="left:27px;top:31px;width:200px">
    <div class="sec-title on-rust" style="margin-bottom:7px">PHYSICAL COMPULSIONS</div>
    <div class="phys-item"><span class="icon"></span><div><h4>Washing</h4><p>Excessive cleaning of hands/body to remove germs, contaminants, or to relieve anxiety about contamination.</p></div></div>
    <div class="phys-item"><span class="icon"></span><div><h4>Checking</h4><p>Repeatedly verifying doors are locked, appliances are off, or re-reading emails to ensure no mistakes. Checking is one of the most common compulsions and can appear in many different forms.</p></div></div>
    <div class="phys-item"><span class="icon"></span><div><h4>Ordering/Arranging</h4><p>Needing items to be placed in a specific order or symmetry to relieve discomfort. This can also include arranging items, clothing, body, etc until it "feels right."</p></div></div>
    <div class="phys-item"><span class="icon"></span><div><h4>Repeating actions</h4><p>Opening and closing doors, tapping, re-walking steps, or rewriting words until it feels "just right," or the intrusive thoughts has been neutralized.</p></div></div>
    <div class="phys-item"><span class="icon"></span><div><h4>Touching/Tapping</h4><p>Touching objects a certain number of times or in a specific pattern to prevent anxiety or a feared outcome. This can coincide with counting compulsions.</p></div></div>
    <div class="phys-item"><span class="icon"></span><div><h4>Reassurance Seeking</h4><p>Repeatedly seeking reassurance from others whether overtly or covertly. This seeks to temporarily "wash away" doubt and fear. This can also look like researching for answers on the internet, reviewing different forums, or excessive doctor visits.</p></div></div>
  </div>
  <svg class="abs" style="left:0;top:398px" width="237" height="230" viewBox="0 0 237 230" aria-hidden="true">
    <path d="M0 230 V120 A150 150 0 0 1 237 70 V230 Z" fill="#7fb3c6"/>
    <path d="M0 230 V140 A132 132 0 0 1 225 92 V230 Z" fill="#f3efe6"/>
  </svg>
  <div class="placeholder" role="img" aria-label="Illustration of a stressed person holding their head beneath a tangled scribble cloud" style="left:40px;top:450px;width:165px;height:178px;border-radius:50% 50% 0 0;background:linear-gradient(180deg,#e9e5dc 0%,#d7c6a4 50%,#3f6d78 100%)"></div>

  <div class="abs body-text" style="left:256px;top:31px;width:202px">
    <div class="sec-title" style="margin-bottom:6px">MENTAL COMPULSIONS</div>
    <p>Mental Compulsions are internal acts that people perform in their minds, such as counting, praying, repeating words silently, replacing a bad thought with a good thought, reviewing a memory, checking and monitoring feelings and thoughts, or performing mental rituals to counteract obsessions or to prevent perceived harm.</p>
    <ul class="bullets">
      <li><b>Counting</b>Repeatedly counting to a certain number to prevent a bad event.</li>
      <li><b>Praying</b>Engaging in prayer rituals to counteract negative thoughts or prevent harm.</li>
      <li><b>Repeating words or phrases</b>Silently saying words, phrases, or prayers to neutralize anxiety.</li>
      <li><b>Reviewing</b>Mentally going over events to ensure nothing bad happened. Or replaying conversations, or reviewing how you feel about something over and over again.</li>
      <li><b>Canceling or Neutralizing</b>Thinking a "good" thought to cancel out a "bad" thought. Or replacing a scary image with a happy image.</li>
      <li><b>List-making</b>Creating lists to make sure important details are not forgotten or to prevent disaster. Or creating a mental list as to why something is okay, then mentally reviewing that list to reassure yourself.</li>
      <li><b>Mental Checking</b>Checking other's responses and facial expressions, checking one's own internal feelings and responses to a particular situation or thought.</li>
    </ul>
    <p><strong>Ruminating (see below)</strong></p>
  </div>
  <div class="abs rumination-box body-text" style="left:253px;top:364px;width:201px;height:240px">
    <div class="t1">RUMINATION AS A</div>
    <div class="t2">COMPULSION</div>
    <p>Rumination, in the context of Obsessive-Compulsive Disorder (OCD), refers to the compulsive process of engaging in prolonged, repetitive thinking about a theme or question related to one's obsessions. Unlike productive problem-solving, ruminating in OCD does not lead to a solution or relief; instead, it exacerbates the cycle of anxiety and compulsive behavior. It is a mental compulsion that individuals with OCD often use in an attempt to resolve or make sense of their intrusive thoughts, but this strategy inevitably becomes a part of the disorder's self-perpetuating cycle. Rumination can have a profound impact on an individual's emotional well-being and quality of life. It can lead to increased anxiety, depression, and feelings of hopelessness, as the individual feels trapped in a cycle of endless thought without escape. Additionally, rumination can detract from one's ability to engage in the present moment, maintain social relationships, and perform daily tasks.</p>
    <ul class="bullets">
      <li>Intrusive and Unwanted: Rumination is often experienced as intrusive &amp; unwanted, much like the initial obsessions that trigger it.</li>
      <li>Individuals may spend hours ruminating over a single thought or question, significantly impacting their daily functioning.</li>
    </ul>
  </div>

  <div class="abs panel-sky" style="left:512px;top:30px;width:426px;height:116px"></div>
  <div class="abs tab-head" style="left:512px;top:30px;width:255px">THE ROLE OF AVOIDANCE IN OCD</div>
  <div class="abs body-text" style="left:524px;top:58px;width:405px">
    <p class="intro-lead" style="font-size:5.8px;margin-bottom:5px">Avoidance plays a crucial role in the maintenance and exacerbation of Obsessive-Compulsive Disorder (OCD) by serving as a maladaptive coping strategy to minimize exposure to feared thoughts, objects, situations, or sensations.</p>
    <p>Individuals with OCD often engage in avoidance behaviors to reduce the anxiety and distress associated with their obsessions. For example, someone with contamination fears might avoid public spaces, touching door handles, or shaking hands to prevent exposure to perceived germs. Although avoidance can provide temporary relief from anxiety, it reinforces the belief in the danger of the avoided stimuli and prevents individuals from learning that their fears are unfounded or exaggerated. This reinforcement cycle keeps the person trapped in the disorder, as avoidance behaviors become increasingly restrictive and limit one's ability to function in daily life. Furthermore, avoidance prevents the opportunity for habituation and the natural reduction of anxiety over time, making it a counterproductive strategy that sustains and can even intensify the OCD cycle.</p>
  </div>

  <div class="abs body-text" style="left:512px;top:163px;width:218px">
    <div class="sec-title" style="margin-bottom:7px">THE OCD CYCLE EXPLAINED</div>
    <p>The OCD cycle is a distressing loop that begins with intrusive, unwanted obsessions that trigger intense anxiety or discomfort. In an attempt to alleviate this distress, individuals engage in compulsive behaviors or mental acts, which are repetitive and often ritualistic actions aimed at neutralizing the obsession or preventing a feared event. Although these compulsions provide temporary relief from anxiety, this relief is short-lived and inadvertently reinforces the obsession, making the individual more likely to engage in the compulsive behavior again when the obsession reoccurs. This cycle—obsession leading to anxiety, followed by compulsive behavior and temporary relief—becomes a self-perpetuating loop that can significantly impair daily functioning and quality of life.</p>
  </div>
  <svg class="abs" style="left:760px;top:150px" width="185" height="170" viewBox="0 0 185 170" aria-label="OCD cycle diagram: intrusive thoughts lead to obsession, distress, compulsion and relief, which loops back">
    <defs><marker id="arrow" viewBox="0 0 6 6" refX="5" refY="3" markerWidth="5" markerHeight="5" orient="auto"><path d="M0 0L6 3L0 6z" fill="var(--ink)"/></marker></defs>
    <text class="cycle-label" x="22" y="28">URGES</text>
    <text class="cycle-label" x="60" y="22">IMPULSES</text>
    <text class="cycle-label" x="100" y="22">IMAGES</text>
    <text class="cycle-label" x="140" y="28">IDEAS</text>
    <text class="cycle-label" x="4" y="50">MEMORIES</text>
    <text class="cycle-label" x="56" y="50">INTRUSIVE THOUGHTS</text>
    <text class="cycle-label" x="140" y="50">SENSATIONS</text>
    <path d="M92 54 V66" stroke="var(--ink)" stroke-width=".6" marker-end="url(#arrow)"/>
    <text class="cycle-label" x="76" y="73">OBSESSION</text>
    <circle cx="92" cy="100" r="22" fill="none" stroke="var(--teal)" stroke-width="1" stroke-dasharray="3 2"/>
    <text class="cycle-label" x="73" y="102">THE OCD CYCLE</text>
    <text class="cycle-label" x="124" y="102">DISTRESS</text>
    <text class="cycle-label" x="140" y="78">MEANING</text>
    <text class="cycle-label" x="140" y="84">ATTACHED</text>
    <text class="cycle-label" x="40" y="102">RELIEF</text>
    <text class="cycle-label" x="0" y="76">NEGATIVE</text>
    <text class="cycle-label" x="0" y="82">REINFORCEMENT</text>
    <path d="M92 124 V130" stroke="var(--ink)" stroke-width=".6" marker-end="url(#arrow)"/>
    <text class="cycle-label" x="74" y="138">COMPULSION</text>
    <text class="cycle-label" x="148" y="134">OVERT</text>
    <text class="cycle-label" x="148" y="140">BEHAVIOUR</text>
    <text class="cycle-label" x="150" y="154">MENTAL</text>
    <text class="cycle-label" x="150" y="160">RITUALS</text>
    <text class="cycle-label" x="28" y="140">AVOIDANCE</text>
    <text class="cycle-label" x="16" y="154">REASSURANCE</text>
    <text class="cycle-label" x="22" y="160">SEEKING</text>
    <path d="M146 132 L120 137" stroke="var(--ink)" stroke-width=".5" marker-end="url(#arrow)"/>
    <path d="M72 136 L56 138" stroke="var(--ink)" stroke-width=".5" marker-end="url(#arrow)"/>
  </svg>

  <div class="abs body-text" style="left:514px;top:302px;width:425px">
    <div class="sec-title dark">THE PROGRESSIVE NATURE OF OCD:</div>
    <div class="sec-title" style="margin-bottom:6px">HOW IT GROWS OVER TIME</div>
    <p>Obsessive-Compulsive Disorder (OCD) is not a static condition; it is dynamic and, without effective intervention, tends to grow more encompassing and debilitating over time. The progression of OCD can be insidious, with its impact expanding gradually, leading to a noticeable shrinkage of an individual's world and an escalation in their levels of anxiety.</p>
    <ul class="bullets" style="margin-top:6px">
      <li><b>Expanding Avoidance and Restrictions</b>As OCD develops, the range of triggers for a person's obsessions and compulsions often broadens. What may start as a singular concern, such as a fear of contamination, can extend to encompass numerous aspects of daily life, including public spaces, personal interactions, and even certain thoughts or feelings. This expansion results in increasing avoidance behaviors, making the individual's world smaller and smaller. Activities and places once enjoyed become off-limits, tethering the person more tightly to their OCD.</li>
      <li><b>Escalating Time Commitment</b>The rituals and compulsions associated with OCD become more time-consuming as the disorder progresses. What initially may have been a brief check or a quick wash can evolve into hours-long rituals, significantly eating into the day. This escalation not only diminishes the time available for productive or enjoyable activities but also contributes to heightened stress and anxiety, as the rituals themselves become more complex and demanding.</li>
      <li><b>Strain on Relationships</b>The impact of OCD on relationships can be profound. The time and energy consumed by the disorder leave less room for social interactions and the maintenance of healthy relationships. Loved ones may struggle to understand or become frustrated by the compulsions and avoidance behaviors, leading to tension and conflict. Additionally, the person with OCD may withdraw from relationships out of embarrassment, guilt, or a desire to conceal their symptoms, further isolating themselves.</li>
      <li><b>Increasing Anxiety and Emotional Toll</b>Paradoxically, while the compulsions and avoidances of OCD are meant to control anxiety, they often serve to increase it over time. The temporary relief they provide reinforces the behavior, but the underlying anxiety not only persists—it grows. The constant battle against intrusive thoughts and the pressure of compulsions contribute to a heightened state of stress, potentially leading to other mental health issues, such as depression or anxiety disorders.</li>
      <li><b>Impairment in Functioning</b>As OCD intensifies, its impact can extend to all areas of life, including academic or job performance, daily routines, and overall quality of life. The disorder can become so consuming that it impairs the individual's ability to function effectively in their roles as a student, employee, partner, parent, or friend.</li>
    </ul>
  </div>
</section>

</body>
</html>
```